Business Card Design for LeafCrest (Farming Devices)

We need Business Cards for our new Company based in Switzerland called "LeafCrest" We develop innovativ products for indoor and outdoor Farming for household and components for vertical farming. Our initial BloomNest gives people the possibility to grow their own food at home all year round. The design should communicate freshness, innovation, health.

```html
<!DOCTYPE html>
<html lang="en">
<head>
<meta charset="utf-8">
<title>LeafCrest Business Card</title>
<link href="https://fonts.googleapis.com/css2?family=Arimo:wght@400;700&display=swap" rel="stylesheet">
<style>
  :root {
    --brand-blue: #0b72b9;
    --brand-green: #6db33f;
    --paper: #ffffff;
    --backdrop: #cfcfcf;
    --text-light: #ffffff;
  }
  * { margin: 0; padding: 0; box-sizing: border-box; }
  html, body {
    width: 1200px;
    height: 788px;
    overflow: hidden;
    background: var(--backdrop);
    font-family: "Arimo", Arial, sans-serif;
  }
  .stage {
    position: relative;
    width: 1200px;
    height: 788px;
  }
  .card {
    position: absolute;
    width: 525px;
    height: 300px;
    border-radius: 22px;
    overflow: hidden;
    box-shadow: 0 10px 24px rgba(0, 0, 0, 0.22);
  }
  .card-front { left: 50px; top: 120px; background: var(--paper); }
  .card-back { left: 625px; top: 368px; background: var(--brand-blue); }

  .front-shape { position: absolute; inset: 0; }

  .brand-name {
    position: absolute;
    display: flex;
    align-items: center;
    gap: 10px;
    font-weight: 700;
    letter-spacing: 0.5px;
  }
  .brand-dot { border-radius: 50%; flex: none; }

  .card-front .brand-name {
    left: 64px;
    top: 58px;
    font-size: 40px;
    line-height: 48px;
    color: var(--brand-green);
  }
  .card-front .brand-dot { width: 15px; height: 15px; background: var(--brand-blue); }

  .person {
    position: absolute;
    left: 92px;
    top: 216px;
    width: 180px;
    text-align: right;
  }
  .person-name {
    color: var(--brand-green);
    font-weight: 700;
    font-size: 17px;
    letter-spacing: 0.4px;
  }
  .person-title {
    color: var(--text-light);
    font-size: 12px;
    margin-top: 3px;
  }
  .divider {
    position: absolute;
    left: 286px;
    top: 178px;
    width: 1px;
    height: 68px;
    background: var(--brand-green);
  }
  .contact-list {
    position: absolute;
    left: 300px;
    top: 176px;
    list-style: none;
  }
  .contact-item {
    display: flex;
    align-items: center;
    gap: 7px;
    color: var(--text-light);
    font-size: 12px;
    line-height: 23px;
  }
  .contact-icon { width: 11px; height: 11px; flex: none; }
  .address {
    position: absolute;
    left: 110px;
    top: 268px;
    color: var(--text-light);
    font-size: 12px;
    letter-spacing: 0.2px;
  }

  .card-back .brand-name {
    left: 0;
    right: 0;
    top: 0;
    bottom: 0;
    justify-content: center;
    font-size: 64px;
    color: var(--text-light);
  }
  .card-back .brand-dot { width: 22px; height: 22px; background: var(--brand-green); }
</style>
</head>
<body>
<main class="stage">
  <section class="card card-front" aria-label="Business card front">
    <svg class="front-shape" width="525" height="300" viewBox="0 0 525 300" aria-hidden="true">
      <path d="M0,215 Q330,190 440,0 L525,0 L525,300 L0,300 Z" fill="var(--brand-blue)"/>
      <path d="M30,203 Q318,175 415,10" fill="none" stroke="var(--brand-green)" stroke-width="3" stroke-linecap="round"/>
    </svg>

    <div class="brand-name"><span class="brand-dot"></span>LeafCrest</div>

    <div class="person">
      <p class="person-name">DANIEL REED</p>
      <p class="person-title">CEO/Founder</p>
    </div>
    <div class="divider"></div>
    <ul class="contact-list">
      <li class="contact-item">
        <svg class="contact-icon" viewBox="0 0 12 12" aria-hidden="true"><path d="M2.5 1 L4.5 1 L5.3 3.4 L4 4.4 Q5 6.8 7.6 8 L8.6 6.7 L11 7.5 L11 9.5 Q11 11 9.5 11 Q1 10 1 2.5 Q1 1 2.5 1 Z" fill="var(--brand-green)"/></svg>
        555-014-2298
      </li>
      <li class="contact-item">
        <svg class="contact-icon" viewBox="0 0 12 12" aria-hidden="true"><rect x="0.5" y="2" width="11" height="8" rx="1" fill="var(--brand-green)"/><path d="M1 2.5 L6 6.5 L11 2.5" fill="none" stroke="var(--brand-blue)" stroke-width="1"/></svg>
        info@leafcrest.com
      </li>
      <li class="contact-item">
        <svg class="contact-icon" viewBox="0 0 12 12" aria-hidden="true"><circle cx="6" cy="6" r="5.5" fill="var(--brand-green)"/><path d="M0.5 6 H11.5 M6 0.5 Q2.5 6 6 11.5 M6 0.5 Q9.5 6 6 11.5" fill="none" stroke="var(--brand-blue)" stroke-width="0.8"/></svg>
        www.leafcrest.com
      </li>
    </ul>
    <p class="address">2150 Meadow Lane Country Name, AB 30412</p>
  </section>

  <section class="card card-back" aria-label="Business card back">
    <div class="brand-name"><span class="brand-dot"></span>LeafCrest</div>
  </section>
</main>
</body>
</html>
```